Executive recruiting firm in need of business card design

Executive recruiting firm looking for a sleek, classy and modern business card design; card itself will be square shape, rounded edges and soft touch paper, our colors are dark blues in the navy color scale, silvers and grays. Reference our website for a better idea of our company's feel and goals at Staffvex.com - our company message is "Employee Engagement Begins at Recruitment" this should be on the card

Industry/Entity Type

Business

```html
<!DOCTYPE html>
<html lang="en">
<head>
<meta charset="utf-8">
<title>Staffvex Business Card</title>
<link href="https://fonts.googleapis.com/css2?family=Roboto:wght@300;400;500&display=swap" rel="stylesheet">
<style>
  :root {
    --navy: #171a4a;
    --white: #ffffff;
    --silver: #9a9aa6;
    --line: #d8d8e0;
    --backdrop: #3b3b3d;
  }
  * { margin: 0; padding: 0; box-sizing: border-box; }
  html, body { width: 1200px; height: 900px; overflow: hidden; }
  body {
    background: var(--backdrop);
    font-family: "Roboto", Arial, sans-serif;
    display: flex;
    align-items: center;
    justify-content: center;
    gap: 40px;
  }
  .card {
    position: relative;
    width: 540px;
    height: 540px;
    border-radius: 30px;
    overflow: hidden;
    flex: none;
  }
  .card--front {
    background: var(--white);
    display: flex;
    flex-direction: column;
    align-items: center;
    justify-content: center;
    gap: 18px;
  }
  .card--back { background: var(--navy); color: var(--white); }

  .brand-name {
    font-weight: 300;
    letter-spacing: 4px;
    line-height: 1;
  }
  .card--front .brand-name { font-size: 64px; color: var(--navy); }
  .message {
    font-weight: 400;
    font-size: 14px;
    letter-spacing: 2px;
    color: var(--silver);
  }

  .card--back .brand-name {
    position: absolute;
    left: 40px;
    top: 44px;
    font-size: 44px;
    color: var(--white);
  }

  .person {
    position: absolute;
    right: 40px;
    top: 160px;
    text-align: right;
  }
  .person__name { font-weight: 500; font-size: 24px; letter-spacing: 0.5px; }
  .person__title { font-weight: 400; font-size: 18px; color: var(--silver); margin-top: 4px; }

  .address {
    position: absolute;
    right: 40px;
    top: 262px;
    text-align: right;
    font-size: 17px;
    line-height: 24px;
  }

  .divider {
    position: absolute;
    left: 40px;
    right: 40px;
    top: 338px;
    height: 1px;
    background: var(--line);
  }

  .phones {
    position: absolute;
    left: 40px;
    top: 360px;
    list-style: none;
    font-size: 16px;
    line-height: 28px;
  }
  .web {
    position: absolute;
    right: 40px;
    top: 360px;
    list-style: none;
    text-align: right;
    font-size: 16px;
    line-height: 28px;
  }
  .row { display: flex; align-items: center; gap: 10px; }
  .web .row { justify-content: flex-end; }
  .icon { width: 18px; height: 18px; fill: var(--silver); flex: none; }
</style>
</head>
<body>

  <section class="card card--front">
    <p class="brand-name">Staffvex</p>
    <p class="message">Employee Engagement Begins at Recruitment</p>
  </section>

  <section class="card card--back">
    <p class="brand-name">Staffvex</p>

    <div class="person">
      <p class="person__name">Daniel Whitford</p>
      <p class="person__title">Managing Director</p>
    </div>

    <p class="address">480 East 200 South<br>Millcreek City 84107</p>

    <div class="divider"></div>

    <ul class="phones">
      <li class="row">
        <svg class="icon" viewBox="0 0 24 24"><path d="M6.6 10.8a15 15 0 0 0 6.6 6.6l2.2-2.2c.3-.3.7-.4 1-.2 1.1.4 2.3.6 3.6.6.6 0 1 .4 1 1V20c0 .6-.4 1-1 1A17 17 0 0 1 3 4c0-.6.4-1 1-1h3.5c.6 0 1 .4 1 1 0 1.3.2 2.5.6 3.6.1.3 0 .7-.2 1z"/></svg>
        801.555.0142
      </li>
      <li class="row">
        <svg class="icon" viewBox="0 0 24 24"><path d="M6 3h12v5H6zM4 9h16a2 2 0 0 1 2 2v6h-4v4H6v-4H2v-6a2 2 0 0 1 2-2zm4 7v3h8v-3z"/></svg>
        801.555.0187
      </li>
    </ul>

    <ul class="web">
      <li class="row">
        mail@staffvex.com
        <svg class="icon" viewBox="0 0 24 24"><path d="M2 5h20v14H2zm2 2v.5l8 5 8-5V7zm0 3v7h16v-7l-8 5z"/></svg>
      </li>
      <li class="row">
        www.staffvex.com
        <svg class="icon" viewBox="0 0 24 24"><path d="M12 2a10 10 0 1 0 0 20 10 10 0 0 0 0-20zm0 2c1 1.2 1.8 3 2.1 5H9.9C10.2 7 11 5.2 12 4zM4.3 11h3.6c0 .7 0 1.3.1 2H4.3a8 8 0 0 1 0-2zm5.6 2a13 13 0 0 1 0-2h4.2a13 13 0 0 1 0 2zm6.1 0c.1-.7.1-1.3.1-2h3.6a8 8 0 0 1 0 2zm-6.1 2h4.2c-.3 2-1.1 3.8-2.1 5-1-1.2-1.8-3-2.1-5z"/></svg>
      </li>
    </ul>
  </section>

</body>
</html>
```